Up to the Challenge? Canadian based consulting company needs a two sided business card design

A Canadian based security risk management consulting company needs a two-sided business card design. What we do is provide advice and guidance related to emergency, security and business continuity management for small, medium and large companies to help ensure the protection of their people, assets, information, services, operations and reputation.

The final design should be simple, only one or two colours, eye catching, professional and one that makes people look at three or more times just because it looks so darn good.

I have include examples of business cards I like.

Target Market(s)

Small, medium and large companies.

Industry/Entity Type

Security

Contact Information for Business Card

Business Card Size: Standard size of 3.5" (89mm) x 2.0" (51mm) - (see full specifications and guides on PRINTA's website if required)
Card Stock: Looking to use PRINTA's Velda 32pt stock textured paper - seam colour either chili red or black
Business Name: The Harrowfield Group
Website: www.theharrowfieldgroup.example
Telephone: (555)214-0397
Name: Dana Forsythe
Position: Principle
e-mail: Dana.Forsythe@theharrowfieldgroup.example

Font styles to use
Serif

Colors
ec1f27
000000
9d9d9d
aaaaaa
606060

Requirements
Must have
• - "The Harrowfield Group" logo (see uploaded files). I have included grey scale and colour versions.
• - Business card details (as above)
Nice to have
• - One side black or grey scale.
• - Other side would likely be white.
• - Everyone likes the silver logo on the black background.
• - Small element of colour i.e. red but I'm leaning more to greyscale.
Should not have
• - A lot of colour. Keep it simple.

```html
<!DOCTYPE html>
<html lang="en">
<head>
<meta charset="utf-8">
<title>The Harrowfield Group – Business Card</title>
<link href="https://fonts.googleapis.com/css2?family=Cinzel:wght@400;600&family=Open+Sans:wght@400;700&display=swap" rel="stylesheet">
<style>
  :root {
    --red: #ec1f27;
    --black: #000000;
    --grey-dark: #606060;
    --grey-mid: #9d9d9d;
    --grey-light: #aaaaaa;
    --paper: #ffffff;
    --backdrop: #d4d4d4;
    --leaf-shade: #1c1c1c;
  }
  * { box-sizing: border-box; margin: 0; padding: 0; }
  html, body {
    width: 1200px; height: 800px; overflow: hidden;
    background: var(--backdrop);
  }
  .sheet {
    width: 1200px; height: 800px;
    display: flex; align-items: center; justify-content: center; gap: 48px;
  }
  .card {
    width: 520px; height: 297px;
    position: relative; overflow: hidden;
    box-shadow: 0 10px 28px rgba(0,0,0,0.18);
  }
  /* Front */
  .card--front {
    background: var(--paper);
    display: flex; align-items: center; justify-content: center;
  }
  .brand {
    display: flex; align-items: center; gap: 16px;
  }
  .brand__mark {
    width: 34px; height: 34px; background: var(--grey-dark);
  }
  .brand__name {
    font-family: "Cinzel", serif; font-weight: 600;
    color: var(--red); font-size: 26px; letter-spacing: 1px; line-height: 1;
  }
  /* Back */
  .card--back {
    background: var(--black);
    color: var(--paper);
    font-family: "Open Sans", sans-serif;
  }
  .card__decor {
    position: absolute; right: -60px; bottom: -90px;
    width: 300px; height: 300px; border-radius: 50%;
    background: var(--leaf-shade);
  }
  .contact {
    position: absolute; left: 48px; top: 74px;
  }
  .contact__name {
    font-size: 15px; font-weight: 700; letter-spacing: 0.5px; text-transform: uppercase;
  }
  .contact__role {
    font-size: 13px; font-weight: 700; color: var(--red); margin-bottom: 12px;
  }
  .contact__list { list-style: none; }
  .contact__item {
    display: flex; align-items: center; gap: 10px;
    font-size: 12.5px; margin-bottom: 9px;
  }
  .contact__icon {
    width: 18px; height: 18px; background: var(--red);
    display: flex; align-items: center; justify-content: center; flex: none;
  }
  .contact__icon svg { width: 12px; height: 12px; }
</style>
</head>
<body>
<main class="sheet">
  <section class="card card--front" aria-label="Card front">
    <div class="brand">
      <span class="brand__mark" aria-hidden="true"></span>
      <span class="brand__name">The Harrowfield Group</span>
    </div>
  </section>

  <section class="card card--back" aria-label="Card back">
    <div class="card__decor" role="img" aria-label="Faint brand decoration"></div>
    <div class="contact">
      <p class="contact__name">Dana Forsythe</p>
      <p class="contact__role">Principle</p>
      <ul class="contact__list">
        <li class="contact__item">
          <span class="contact__icon"><svg viewBox="0 0 24 24" fill="#fff"><path d="M6.6 10.8a15 15 0 0 0 6.6 6.6l2.2-2.2c.3-.3.7-.4 1-.2 1.1.4 2.3.6 3.6.6.6 0 1 .4 1 1V20c0 .6-.4 1-1 1A17 17 0 0 1 3 4c0-.6.4-1 1-1h3.5c.6 0 1 .4 1 1 0 1.3.2 2.5.6 3.6.1.3 0 .7-.2 1z"/></svg></span>
          (555)214-0397
        </li>
        <li class="contact__item">
          <span class="contact__icon"><svg viewBox="0 0 24 24" fill="none" stroke="#fff" stroke-width="2.4"><rect x="3" y="5" width="18" height="14"/><path d="M3 6l9 7 9-7"/></svg></span>
          Dana.Forsythe@theharrowfieldgroup.example
        </li>
        <li class="contact__item">
          <span class="contact__icon"><svg viewBox="0 0 24 24" fill="none" stroke="#fff" stroke-width="2.2"><circle cx="12" cy="12" r="9"/><path d="M3 12h18M12 3c3 3 3 15 0 18M12 3c-3 3-3 15 0 18"/></svg></span>
          www.theharrowfieldgroup.example
        </li>
      </ul>
    </div>
  </section>
</main>
</body>
</html>
```